Manufacturer of Medical Devices needs a clean & modern packaging for its Red Light Therapy Pr...

We are an innovative startup company developing a new emerging technology to treat pain and help with recovery through the use of red and infrared light. We are looking for a packaging design for this device. Please read the word document attached for detailed instructions.

For the background of the box we prefer black or silver color

```html
<!DOCTYPE html>
<html lang="en">
<head>
<meta charset="utf-8">
<title>Inner Box – Dieline</title>
<link rel="stylesheet" href="https://fonts.googleapis.com/css2?family=Source+Sans+3:wght@300;400&family=Tinos&display=swap">
<style>
  :root {
    --paper: #ffffff;
    --board: #000000;
    --fold: #1e8fd0;
    --dim: #e60012;
    --ink: #111111;
    --brand: #ffffff;
  }
  html, body {
    margin: 0;
    padding: 0;
    overflow: hidden;
    background: var(--paper);
  }
  .sheet {
    position: relative;
    width: 1200px;
    height: 768px;
    background: var(--paper);
    overflow: hidden;
  }
  .sheet__title {
    position: absolute;
    left: 0;
    width: 1242px;
    top: 44px;
    margin: 0;
    text-align: center;
    font: 300 42px/1 "Source Sans 3", sans-serif;
    color: var(--ink);
  }
  .dieline {
    position: absolute;
    inset: 0;
  }
  .board { fill: var(--board); }
  .fold-line { fill: none; stroke: var(--fold); stroke-width: 0.8; }
  .dim-line { stroke: var(--dim); stroke-width: 0.6; fill: none; }
  .dim-arrow { fill: var(--dim); }
  .dim-label {
    fill: var(--dim);
    font: 18px "Tinos", serif;
    text-anchor: middle;
  }
  .brand-name {
    fill: var(--brand);
    font: 400 15px "Source Sans 3", sans-serif;
    letter-spacing: 4px;
    text-anchor: middle;
  }
</style>
</head>
<body>
<main class="sheet">
  <h1 class="sheet__title">inner box</h1>

  <svg class="dieline" width="1200" height="768" viewBox="0 0 1200 768" xmlns="http://www.w3.org/2000/svg">
    <path class="board" d="M261.5 113.5 H994.5 V271.5 H1152 V473 H994.5 V631 H261.5 V473 H104 V271.5 H261.5 Z"/>

    <rect class="fold-line" x="275.5" y="127.5" width="705" height="489.5"/>
    <rect class="fold-line" x="117.5" y="285" width="1020.5" height="174"/>

    <g class="brand brand--left">
      <text class="brand-name" transform="translate(200 372) rotate(-90)">ORVANE</text>
    </g>
    <g class="brand brand--right">
      <text class="brand-name" transform="translate(1056 372) rotate(90)">ORVANE</text>
    </g>

    <g class="dims dims--vertical">
      <line class="dim-line" x1="57" y1="127" x2="86" y2="127"/>
      <line class="dim-line" x1="57" y1="285" x2="86" y2="285"/>
      <line class="dim-line" x1="57" y1="459" x2="86" y2="459"/>
      <line class="dim-line" x1="57" y1="617" x2="86" y2="617"/>
      <line class="dim-line" x1="71.5" y1="127" x2="71.5" y2="617"/>

      <polygon class="dim-arrow" points="71.5,127 66.5,137 76.5,137"/>
      <polygon class="dim-arrow" points="71.5,285 66.5,275 76.5,275"/>
      <polygon class="dim-arrow" points="71.5,285 66.5,295 76.5,295"/>
      <polygon class="dim-arrow" points="71.5,459 66.5,449 76.5,449"/>
      <polygon class="dim-arrow" points="71.5,459 66.5,469 76.5,469"/>
      <polygon class="dim-arrow" points="71.5,617 66.5,607 76.5,607"/>

      <text class="dim-label" transform="translate(47 282) rotate(-90)">113 mm</text>
      <text class="dim-label" transform="translate(47 447) rotate(-90)">125 mm</text>
      <text class="dim-label" transform="translate(47 614) rotate(-90)">113 mm</text>
    </g>

    <g class="dims dims--horizontal">
      <line class="dim-line" x1="117.5" y1="638" x2="117.5" y2="668"/>
      <line class="dim-line" x1="275" y1="638" x2="275" y2="668"/>
      <line class="dim-line" x1="980" y1="638" x2="980" y2="668"/>
      <line class="dim-line" x1="1138" y1="638" x2="1138" y2="668"/>
      <line class="dim-line" x1="117.5" y1="653" x2="1138" y2="653"/>

      <polygon class="dim-arrow" points="117.5,653 127.5,648 127.5,658"/>
      <polygon class="dim-arrow" points="275,653 265,648 265,658"/>
      <polygon class="dim-arrow" points="275,653 285,648 285,658"/>
      <polygon class="dim-arrow" points="980,653 970,648 970,658"/>
      <polygon class="dim-arrow" points="980,653 990,648 990,658"/>
      <polygon class="dim-arrow" points="1138,653 1128,648 1128,658"/>

      <text class="dim-label" x="196" y="686">113 mm</text>
      <text class="dim-label" x="628" y="686">505 mm</text>
      <text class="dim-label" x="1059" y="686">113 mm</text>
    </g>
  </svg>
</main>
</body>
</html>
```